Revise my existing consulting brief with new logo

I just got a logo from Plume Forge for my new management consulting business, and would like to add it to my existing consulting brief, both 1 and 2 page versions, and would like to improve the layout of these documents to make them look more professional. These documents are essentially the brochure or flyer for my business, so they need to be easy to read and understand quickly. I would like these to be either ppt or Word format so that I can update wording in future, and so that I can save to pdf when I want to share with prospective clients. My new logo print file is attached here, as well as the consulting brief documents that need new layout.
Colors and layout used in the revised consulting brief that you will produce should be aligned to the new logo
Updates

Many of you proposed designs that took into account just one of the 2 documents I sent. However, please be advised that I am looking for designs for both documents that I sent, which are 1- and 2-paged versions of my consulting brief, which is essentially a flyer or brochure that explains my consulting service.

This should not look like a resume, but should be more attractive as a kind of business flyer/brochure.

Please also be aware that I am open to landscape format designs, not just portrait, which would be more in line with the versions I sent you.

Target Market(s)

Pharmaceutical and medical device companies

Industry/Entity Type

Pharmaceutical and medical device

Font styles to use
Serif
Sans Serif

Requirements
Must have
• Color and look that align to my new logo. Ability for me to update the text later on my own as needed, so that I can adapt it to different clients.
Should not have
• I am not looking for a PowerPoint template or stationary to match my logo. I am just looking to have the consulting briefs that I sent revised so that they fit the new logo and look more professional in layout.

```html
<!DOCTYPE html>
<html lang="en">
<head>
<meta charset="utf-8">
<title>Clearpath Advisory – Consulting Brief</title>
<link href="https://fonts.googleapis.com/css2?family=Arimo:wght@400;700&family=Archivo+Black&display=swap" rel="stylesheet">
<style>
  :root{
    --navy:#223a78;
    --teal:#17b9bf;
    --teal-dark:#13a6ab;
    --grey-band:#dcdde1;
    --body:#5a5f6a;
    --white:#ffffff;
    --stage:#ecebe8;
  }
  *{box-sizing:border-box;margin:0;padding:0}
  html,body{width:1200px;height:1200px;overflow:hidden;background:var(--stage)}
  body{font-family:"Arimo",Arial,sans-serif;position:relative}
  .flyer{position:absolute;left:194px;top:26px;width:812px;height:1148px;background:var(--white);overflow:hidden;box-shadow:0 2px 10px rgba(0,0,0,.12)}
  .flyer-bg{position:absolute;inset:0}
  .tagline{position:absolute;left:44px;color:var(--teal);font-weight:700;font-size:21px}
  .tagline.first{top:64px}
  .tagline.second{top:117px}
  .brand{position:absolute;left:530px;top:70px;display:flex;align-items:center;gap:12px}
  .brand-dot{width:34px;height:34px;border-radius:50%;background:var(--teal)}
  .brand-name{color:var(--white);font-weight:700;font-size:24px;line-height:1.1;letter-spacing:.5px}
  .header-rule{position:absolute;left:34px;top:195px;width:744px;height:2px;background:var(--teal)}
  .intro{position:absolute;left:52px;top:214px;width:706px;color:var(--white);font-size:14.6px;line-height:19.6px;text-align:justify}
  .service{position:absolute;left:33px;width:445px}
  .service h2{color:var(--teal);font-weight:700;font-size:21.5px;line-height:22px;padding-bottom:3px;border-bottom:1.5px solid var(--navy);width:327px;margin-bottom:6px}
  .service ul{list-style:none}
  .service li{position:relative;padding-left:12px;color:var(--body);font-size:14.4px;line-height:18px;margin-bottom:10px}
  .service li::before{content:"";position:absolute;left:2px;top:7px;width:5px;height:5px;border-radius:50%;background:var(--navy)}
  .service.ira{top:451px}
  .service.ma{top:694px}
  .service.transform{top:859px}
  .profile-card{position:absolute;left:492px;top:308px;width:277px;height:738px}
  .profile-card svg{position:absolute;inset:0}
  .profile-text{position:absolute;left:0;right:0;top:310px;text-align:center;padding:0 10px}
  .profile-name{font-family:"Archivo Black","Arimo",sans-serif;color:var(--white);font-size:36px;line-height:38px;letter-spacing:.5px}
  .profile-role{color:var(--white);font-weight:700;font-size:20px;margin-top:4px}
  .profile-points p{color:var(--navy);font-size:15px;line-height:19.2px;margin-top:19px}
  .profile-points p:first-child{margin-top:13px}
  .footer-handle{position:absolute;left:57px;top:1099px;display:flex;align-items:center;gap:8px;color:var(--navy);font-size:26px}
  .footer-handle .icon{width:28px;height:28px;border-radius:50%;background:var(--navy)}
  .footer-contact{position:absolute;left:358px;top:1101px;width:454px;height:27px;background:var(--navy);border-radius:6px 0 0 6px;color:var(--white);font-size:19px;line-height:27px;padding-left:16px;letter-spacing:.3px}
</style>
</head>
<body>
<main class="flyer">
  <svg class="flyer-bg" width="812" height="1148" viewBox="0 0 812 1148" aria-hidden="true">
    <polygon points="0,292 491,452 491,520 0,300" fill="var(--grey-band)"/>
    <polygon points="0,294 491,446 491,492" fill="var(--teal)"/>
    <polygon points="812,380 700,420 812,400" fill="var(--grey-band)"/>
    <polygon points="812,286 640,400 812,374" fill="var(--teal)"/>
    <polygon points="0,0 812,0 812,286 640,400 491,452 0,292" fill="var(--navy)"/>
  </svg>

  <p class="tagline first">Solving complex challenges</p>
  <p class="tagline second">Driving programs from strategy to action</p>

  <div class="brand">
    <span class="brand-dot"></span>
    <span class="brand-name">Clearpath<br>Advisory LLC</span>
  </div>

  <div class="header-rule"></div>

  <p class="intro">Margaret Ellison helps companies tackle and succeed in making change by providing project leadership and program management services for key business objectives. She understands the importance of getting it right the first time and specializes in shaping solutions to drive complex business initiatives from strategy to action.</p>

  <section class="service ira">
    <h2>Inflation Reduction Act</h2>
    <ul>
      <li>Drug price negotiation operational readiness: Put in place process and governance for submission development and ensuing engagements with CMS. Identify cross-functional team members needed, design approval processes, lead change management, build and oversee integrated project plan and timeline.</li>
      <li>Part D redesign readiness: Identify gaps and develop plan to address, including chartering workstreams and creation and implementation of plans and timelines to drive from strategy to execution.</li>
    </ul>
  </section>

  <section class="service ma">
    <h2>Mergers &amp; Acquisitions</h2>
    <ul>
      <li>For companies acquiring a target: Build integration teams, lead team in developing integration plan &amp; budget, facilitate planning for an efficient and effective Day 1, and for 30-60-90-day horizon.</li>
      <li>Assist companies looking to be acquired to prepare their people, processes and systems for due diligence</li>
    </ul>
  </section>

  <section class="service transform">
    <h2>Strategic Programs &amp;<br>Business Transformation</h2>
    <ul>
      <li>Develop strategy, framework and governance to accomplish organization and business model change, inclusive of people, processes and systems.</li>
      <li>Change Management for new ways of working and new business models.</li>
      <li>Facilitate goal-setting and strategic prioritization exercises with leadership teams.</li>
    </ul>
  </section>

  <aside class="profile-card">
    <svg width="277" height="738" viewBox="0 0 277 738">
      <defs>
        <linearGradient id="portraitTone" x1="0" y1="0" x2="0" y2="1">
          <stop offset="0" stop-color="#a7a6a3"/>
          <stop offset="1" stop-color="#cfc8bd"/>
        </linearGradient>
      </defs>
      <path d="M0,160 L0,718 Q0,738 20,738 L257,738 Q277,738 277,718 L277,160 Z" fill="var(--teal)"/>
      <path d="M138.5,0 L262,64 Q277,72 277,90 L277,210 Q277,228 262,236 L138.5,301 L15,236 Q0,228 0,210 L0,90 Q0,72 15,64 Z" fill="var(--white)"/>
      <path role="img" aria-label="Portrait photo of Margaret Ellison, principal consultant" d="M138.5,10 L258,72 Q268,78 268,92 L268,208 Q268,222 258,228 L138.5,291 L19,228 Q9,222 9,208 L9,92 Q9,78 19,72 Z" fill="url(#portraitTone)"/>
    </svg>
    <div class="profile-text">
      <h1 class="profile-name">MARGARET<br>ELLISON</h1>
      <p class="profile-role">Principal</p>
      <div class="profile-points">
        <p>25 years of Pharmaceutical and MedTech expertise at Halvern Health.</p>
        <p>Robust strategy and marketing background.</p>
        <p>Enhances business transformations by infusing customer-centric insights, effective communication, and commercial focus.</p>
        <p>Uncovers new solutions, connects the dots, builds strong cross-functional relationships, and drives engagement across teams.</p>
      </div>
    </div>
  </aside>

  <div class="footer-handle"><span class="icon"></span>margaret-ellison</div>
  <div class="footer-contact">m.ellison.advisory@example.com | 555 014 2278</div>
</main>
</body>
</html>
```